Relaxation, deep tissue sports massage

We need an opening of anew massage centre poster
relaxation, deep tissue and sports massage
POSTER SIZE A4 and for a 1meter X 1meter stand
the business name is Toverin , we have a logo already , which i enclose
the poster needs to be eye catching
location Brindle Lane Medical Clinic 0872914658 for an appointment
location uHealth on Tarrowby 0873195246 for an appointment

Target Market(s)

public

Industry/Entity Type

Massage

Requirements
Must have
• logo , be vibrant ,eye catching and inviting
Nice to have
• massage picture , logo etc

```html
<!DOCTYPE html>
<html lang="en">
<head>
<meta charset="utf-8">
<title>Toverin massage poster</title>
<link rel="stylesheet" href="https://fonts.googleapis.com/css2?family=Montserrat:wght@400;500&family=Cormorant+Garamond:ital,wght@1,500&display=swap">
<style>
  :root {
    --sky: #17a8de;
    --sky-deep: #0a8cc4;
    --sky-dark: #0b86bd;
    --lime: #8cc63f;
    --blush: #f2d3c6;
    --cream: #fbf7f2;
    --ink: #1d2a33;
    --white: #ffffff;
    --light: #fff6e6;
    --gold: #efc98f;
    --peach: #f2b48e;
    --rose: #e69a7a;
    --tan: #d9a07a;
  }
  * { margin: 0; padding: 0; box-sizing: border-box; }
  html, body { width: 855px; height: 1200px; overflow: hidden; background: var(--white); }
  .poster {
    position: relative;
    width: 855px;
    height: 1200px;
    overflow: hidden;
    background: linear-gradient(160deg, var(--sky) 0%, var(--sky) 60%, var(--sky-dark) 100%);
  }
  .hero-photo {
    position: absolute;
    left: 0; top: 0;
    width: 855px; height: 860px;
    background:
      radial-gradient(ellipse 260px 200px at 480px 470px, rgba(230,154,122,0.75) 0%, rgba(230,154,122,0) 70%),
      radial-gradient(ellipse 360px 300px at 470px 400px, rgba(242,180,142,0.95) 0%, rgba(242,180,142,0) 72%),
      radial-gradient(ellipse 260px 260px at 200px 260px, rgba(239,201,143,0.95) 0%, rgba(239,201,143,0) 70%),
      radial-gradient(ellipse 220px 420px at 790px 360px, rgba(217,160,122,0.9) 0%, rgba(217,160,122,0) 70%),
      radial-gradient(ellipse 300px 160px at 700px 80px, rgba(230,170,130,0.7) 0%, rgba(230,170,130,0) 70%),
      radial-gradient(ellipse 380px 180px at 160px 60px, var(--light) 0%, rgba(255,246,230,0) 75%),
      radial-gradient(ellipse 320px 160px at 250px 640px, rgba(245,210,180,0.9) 0%, rgba(245,210,180,0) 70%),
      linear-gradient(180deg, #f6e6d0 0%, #efcfae 45%, #eec0a0 70%, #f1ddc9 100%);
  }
  .waves {
    position: absolute;
    left: 0; top: 0;
    width: 855px; height: 1200px;
  }
  .brand {
    position: absolute;
    left: 0; top: 688px;
    width: 855px;
    text-align: center;
  }
  .brand-name {
    display: inline-flex;
    align-items: center;
    gap: 14px;
    font-family: "Montserrat", sans-serif;
    font-weight: 500;
    font-size: 44px;
    color: var(--sky);
    letter-spacing: 0.5px;
  }
  .brand-dot {
    width: 22px; height: 22px;
    border-radius: 50%;
    background: var(--lime);
  }
  .brand-tagline {
    margin-top: 0;
    font-family: "Cormorant Garamond", serif;
    font-style: italic;
    font-weight: 500;
    font-size: 25px;
    color: var(--ink);
    letter-spacing: 0.5px;
  }
  .services {
    position: absolute;
    left: 0; top: 928px;
    width: 855px;
    display: flex;
    justify-content: center;
    align-items: center;
    font-family: "Montserrat", sans-serif;
    font-weight: 400;
    font-size: 27px;
    letter-spacing: 1.5px;
    color: var(--white);
  }
  .services .sep {
    display: inline-block;
    width: 8px; height: 8px;
    border-radius: 50%;
    background: var(--lime);
    margin: 0 24px;
  }
  .locations {
    position: absolute;
    left: 0; top: 1032px;
    width: 855px;
    height: 115px;
  }
  .location {
    position: absolute;
    top: 4px;
    color: var(--white);
  }
  .location--left { right: 427px; text-align: right; }
  .location--right { left: 476px; text-align: left; }
  .location-name {
    font-family: "Cormorant Garamond", serif;
    font-style: italic;
    font-weight: 500;
    font-size: 27px;
    line-height: 1.2;
    margin-bottom: 10px;
  }
  .location-call {
    font-family: "Montserrat", sans-serif;
    font-size: 21px;
    line-height: 1.3;
  }
  .divider {
    position: absolute;
    left: 451px; top: 0;
    width: 3px; height: 112px;
    background: var(--lime);
  }
</style>
</head>
<body>
<main class="poster">
  <div class="hero-photo" role="img" aria-label="Photograph of a smiling woman relaxing on a massage table while receiving a back massage"></div>

  <svg class="waves" viewBox="0 0 613 860" preserveAspectRatio="none" aria-hidden="true">
    <path d="M0,470 C150,520 420,520 613,440 L613,860 L0,860 Z" fill="var(--cream)"/>
    <path d="M0,555 C200,610 430,570 613,470 L613,860 L0,860 Z" fill="var(--lime)"/>
    <path d="M0,590 C200,640 440,590 613,505 L613,860 L0,860 Z" fill="var(--sky-deep)"/>
    <path d="M0,605 C210,655 450,610 613,540 L613,860 L0,860 Z" fill="var(--sky)"/>
    <path d="M150,628 C330,640 480,610 613,565 L613,585 C480,625 330,650 150,628 Z" fill="var(--blush)"/>
    <path d="M150,628 C330,650 480,630 613,590 L613,600 C480,640 330,655 150,628 Z" fill="var(--white)" opacity="0.85"/>
  </svg>

  <div class="brand">
    <div class="brand-name">Toverin massage<span class="brand-dot"></span></div>
    <div class="brand-tagline">Relax Renew Revive</div>
  </div>

  <p class="services">relaxation<span class="sep"></span>deep tissue<span class="sep"></span>sports massage</p>

  <section class="locations">
    <div class="location location--left">
      <p class="location-name">Brindle Lane Medical Clinic</p>
      <p class="location-call">call 0872914658<br>to make an appointment</p>
    </div>
    <div class="divider"></div>
    <div class="location location--right">
      <p class="location-name">uHealth on Tarrowby</p>
      <p class="location-call">call 0873195246<br>to make an appointment</p>
    </div>
  </section>
</main>
</body>
</html>
```